Clearwave Motion Florida Billboard

We need a billboard designed for our physical therapy practice. Our billboard also serves as the sign for our building. We would like to have some sort of graphic notifying people driving by that our building is located here. Please go to www.clearwavemotionfl.example in order to get a better idea of our company.

Target Market(s)

Senior citizens having physical therapy

Industry/Entity Type

Healthcare- Physical Therapy

Colors
0094D4
00A9DD
6FCCEA
C7EBF8
E9F6FB

Requirements
Must have
• Must contain in bold the words "physical therapy". Must be highly visible from the road and have our company colors incorporated. Would also like to use the phrase "Relieving Pain. Restoring Function. Improving Lives."

```html
<!DOCTYPE html>
<html lang="en">
<head>
<meta charset="utf-8">
<title>Clearwave Motion Florida Billboard</title>
<link href="https://fonts.googleapis.com/css2?family=Roboto:wght@400;500;700&family=Montserrat:wght@500&display=swap" rel="stylesheet">
<style>
  :root {
    --brand-deep: #0072c0;
    --brand-blue: #0094d4;
    --brand-sky: #00a9dd;
    --brand-light: #6fccea;
    --brand-pale: #c7ebf8;
    --brand-mist: #e9f6fb;
    --band: #1591be;
    --ink: #111418;
    --name-ink: #3a3a3a;
    --arrow: #7f97a4;
    --white: #ffffff;
    --stage: #d9dcdf;
  }
  * { margin: 0; padding: 0; box-sizing: border-box; }
  html, body {
    width: 1200px; height: 684px; overflow: hidden;
    background: var(--stage);
    font-family: "Roboto", sans-serif;
  }
  .billboard {
    position: absolute; left: 20px; top: 110px;
    width: 1160px; height: 464px; overflow: hidden;
    background: var(--white);
  }
  .photo-area {
    position: absolute; left: 0; top: 0; width: 600px; height: 464px;
    background: linear-gradient(135deg, var(--brand-light) 0%, var(--brand-deep) 35%, var(--brand-blue) 65%, var(--brand-sky) 100%);
  }
  .panels { position: absolute; left: 0; top: 0; }
  .tagline {
    position: absolute; color: var(--white);
    font-size: 23px; font-weight: 500; letter-spacing: -0.4px; white-space: nowrap;
  }
  .tagline.pain { right: 686px; top: 24px; }
  .tagline.function { left: 271px; top: 69px; }
  .tagline.lives { left: 292px; top: 114px; }
  .tagline-rule { position: absolute; height: 2px; background: var(--white); }
  .tagline-rule.first { left: 292px; top: 59px; width: 194px; }
  .tagline-rule.second { left: 271px; top: 105px; width: 200px; }
  .brand-dot {
    position: absolute; left: 765px; top: 34px; width: 130px; height: 130px;
    border-radius: 50%; background: var(--brand-sky);
  }
  .brand-divider {
    position: absolute; left: 911px; top: 30px; width: 3px; height: 137px;
    background: var(--name-ink);
  }
  .brand-name {
    position: absolute; left: 933px; top: 42px;
    font-family: "Montserrat", sans-serif; font-weight: 500;
    color: var(--name-ink); letter-spacing: 1.5px; line-height: 1.15;
    white-space: nowrap;
  }
  .brand-name .line { display: block; font-size: 27px; }
  .brand-name .line.region { font-size: 19px; letter-spacing: 2px; margin-top: 8px; }
  .headline {
    position: absolute; left: 462px; top: 197px; width: 698px; height: 89px;
    display: flex; align-items: center; justify-content: center;
    color: var(--white); font-weight: 700; font-size: 62px; letter-spacing: -0.5px;
    padding-left: 12px; white-space: nowrap;
  }
  .contact {
    position: absolute; left: 712px; display: flex; align-items: center; gap: 10px;
    color: var(--ink); font-weight: 700; white-space: nowrap;
  }
  .contact.web { top: 324px; font-size: 23px; letter-spacing: -0.2px; }
  .contact.phone { top: 376px; font-size: 46px; }
  .contact svg { flex: none; }
</style>
</head>
<body>
  <main class="billboard">
    <div class="photo-area" role="img" aria-label="Photo of a therapist in scrubs guiding a patient's knee stretch on an exercise mat"></div>

    <svg class="panels" width="1160" height="464" viewBox="0 0 1160 464" aria-hidden="true">
      <defs>
        <clipPath id="info-panel-clip">
          <path d="M511,0 L1160,0 L1160,464 L556,464 C500,400 462,320 462,240 C462,140 482,60 511,0 Z"/>
        </clipPath>
      </defs>
      <path d="M511,0 L1160,0 L1160,464 L556,464 C500,400 462,320 462,240 C462,140 482,60 511,0 Z" fill="var(--white)"/>
      <g clip-path="url(#info-panel-clip)">
        <rect x="440" y="197" width="720" height="89" fill="var(--band)"/>
        <rect x="440" y="286" width="720" height="178" fill="var(--brand-pale)"/>
      </g>
      <g class="location-pointer">
        <line x1="545" y1="369" x2="615" y2="369" stroke="var(--arrow)" stroke-width="5"/>
        <path d="M529,369 L568,345 L556,369 L568,393 Z" fill="var(--arrow)"/>
        <circle cx="637" cy="369" r="27" fill="var(--arrow)" opacity="0.55"/>
        <circle cx="637" cy="369" r="20" fill="var(--arrow)"/>
        <path d="M637,382 C631,374 629,370 629,366 A8,8 0 0 1 645,366 C645,370 643,374 637,382 Z" fill="#35505e"/>
        <circle cx="637" cy="366" r="3" fill="var(--arrow)"/>
      </g>
    </svg>

    <p class="tagline pain">Relieving Pain</p>
    <div class="tagline-rule first"></div>
    <p class="tagline function">Restoring Function</p>
    <div class="tagline-rule second"></div>
    <p class="tagline lives">Improving Lives</p>

    <div class="brand-dot" aria-hidden="true"></div>
    <div class="brand-divider" aria-hidden="true"></div>
    <h1 class="brand-name">
      <span class="line">CLEARWAVE</span>
      <span class="line">MOTION</span>
      <span class="line region">FLORIDA</span>
    </h1>

    <h2 class="headline">PHYSICAL THERAPY</h2>

    <p class="contact web">
      <svg width="28" height="28" viewBox="0 0 24 24" aria-hidden="true" fill="none" stroke="var(--ink)" stroke-width="2">
        <circle cx="12" cy="12" r="10"/>
        <ellipse cx="12" cy="12" rx="4.5" ry="10"/>
        <line x1="2" y1="12" x2="22" y2="12"/>
        <line x1="4" y1="6.5" x2="20" y2="6.5"/>
        <line x1="4" y1="17.5" x2="20" y2="17.5"/>
      </svg>
      www.clearwavemotionfl.example
    </p>
    <p class="contact phone">
      <svg width="28" height="28" viewBox="0 0 24 24" aria-hidden="true">
        <path fill="var(--ink)" d="M6.6 10.8a15.1 15.1 0 0 0 6.6 6.6l2.2-2.2c.3-.3.7-.4 1-.2 1.1.4 2.300.6 3.6.6.6 0 1 .4 1 1V20c0 .6-.4 1-1 1A17 17 0 0 1 3 4c0-.6.4-1 1-1h3.5c.6 0 1 .4 1 1 0 1.3.2 2.5.6 3.6.1.3 0 .7-.2 1z"/>
        <path fill="none" stroke="var(--ink)" stroke-width="1.8" d="M14 6.5a4 4 0 0 1 3.5 3.5M14 2.5a8 8 0 0 1 7.5 7.5"/>
      </svg>
      941-555-0187
    </p>
  </main>
</body>
</html>
```